Wild Mo's Wine Label Project

We need a new entry level wine label called "Wild Mo's" for a range of wines we are developing from inland Australia. Our company is made up of three youngish guys who live hard and love taking the mickey. Wild Mo is Wild Moss - the largest and loudest of the three partners (and ideally this label will take the mickey out of him). We've grown the grapes ourselves for this first release which will be a 2012 Pinot Gris. Wine style is dry, young, fresh and contemporary and pitched at the sub AUD $10 retail price point. The package will be flint (clear) claret shape bottle with plain screwcap (colour matched to suit the winning label design).

I've attached a couple of photos of Wild Moss to give you some idea of his presence and persona.

Target Market(s)

Semi educated 25 - 40 year old wine drinkers. Skewed towards females.

Industry/Entity Type

Retail

Requirements
Should not have
• Anything traditional or old fashioned

```html
<!DOCTYPE html>
<html lang="en">
<head>
<meta charset="utf-8">
<title>Wild Mo's 2012 Pinot Gris Label</title>
<link rel="stylesheet" href="https://fonts.googleapis.com/css2?family=Cinzel:wght@400;700&display=swap">
<style>
  :root {
    --stage-light: #b3c42a;
    --stage-dark: #4d5f1c;
    --shield-black: #050608;
    --shield-rim: #8c5a28;
    --shield-inner-rim: #2f7fc0;
    --ribbon-black: #07080c;
    --ribbon-navy: #1b1f6a;
    --ribbon-blue: #3a8fd4;
    --text-white: #ffffff;
    --name-blue: #3aa3e0;
  }
  html, body {
    margin: 0;
    padding: 0;
    width: 1200px;
    height: 1200px;
    overflow: hidden;
  }
  body {
    background: radial-gradient(ellipse at 50% 30%, var(--stage-light) 0%, var(--stage-dark) 85%);
  }
  .label-art {
    position: absolute;
    inset: 0;
    width: 1200px;
    height: 1200px;
  }
  .vintage, .varietal {
    font-family: "Cinzel", serif;
    font-weight: 400;
    fill: var(--text-white);
    text-anchor: middle;
  }
  .vintage { font-size: 46px; }
  .varietal { font-size: 38px; letter-spacing: 1px; }
  .brand-name {
    font-family: "Cinzel", serif;
    font-weight: 700;
    fill: var(--name-blue);
    text-anchor: middle;
  }
</style>
</head>
<body>
<svg class="label-art" viewBox="0 0 1200 1200" xmlns="http://www.w3.org/2000/svg">
  <defs>
    <linearGradient id="ribbonLeftFill" x1="0" y1="0" x2="1" y2="0">
      <stop offset="0" stop-color="var(--ribbon-blue)"/>
      <stop offset="0.35" stop-color="var(--ribbon-navy)"/>
      <stop offset="1" stop-color="var(--ribbon-black)"/>
    </linearGradient>
    <linearGradient id="ribbonRightFill" x1="1" y1="0" x2="0" y2="0">
      <stop offset="0" stop-color="var(--ribbon-blue)"/>
      <stop offset="0.35" stop-color="var(--ribbon-navy)"/>
      <stop offset="1" stop-color="var(--ribbon-black)"/>
    </linearGradient>
  </defs>

  <g class="ribbon" role="img" aria-label="Black ribbon with blue sunburst rays and folded ends">
    <polygon class="ribbon-band" points="120,410 380,410 380,560 120,560" fill="url(#ribbonLeftFill)"/>
    <polygon class="ribbon-fold" points="95,440 120,410 120,560 95,590" fill="var(--ribbon-blue)"/>
    <polygon class="ribbon-band" points="820,410 1080,410 1080,560 820,560" fill="url(#ribbonRightFill)"/>
    <polygon class="ribbon-fold" points="1105,440 1080,410 1080,560 1105,590" fill="var(--ribbon-blue)"/>
  </g>

  <path class="shield" d="M365,350 Q600,300 835,350 L835,620 Q835,780 600,885 Q365,780 365,620 Z"
        fill="var(--shield-black)" stroke="var(--shield-rim)" stroke-width="12" stroke-linejoin="round"/>
  <path class="shield-inner-rim" d="M380,362 Q600,316 820,362 L820,620 Q820,770 600,868 Q380,770 380,620 Z"
        fill="none" stroke="var(--shield-inner-rim)" stroke-width="3"/>

  <text class="vintage" x="600" y="395">2012</text>
  <text class="varietal" x="600" y="440">PINOT GRIS</text>

  <text class="brand-name" x="600" y="580" font-size="104">WILD</text>
  <text class="brand-name" x="600" y="745" font-size="150">MO</text>
</svg>
</body>
</html>
```